依頼詳細
オープンして3年弱になりますがまだまだお店の知名度が低いので
駅前で配ったり、新聞の折り込みに入れたりしたいです。
ターゲットは女性のお客様ですが、家族で犬を飼われてることが多く
家族にも対応したチラシが希望です
記載項目
店名
ロゴ
電話
ブログのサイト
料金
店長のプロフィール
クーポンなど
サイズ
A4
ページ数
両面
希望イメージ
シンプル 複雑
単色 カラフル
暗い 明るい
日常 高級
遊び心 厳粛
未来的 伝統的
女性的 男性的
希望する色
青系
オープンして2年半が経ちましたが
新規のお客様を募集するチラシです

表面にクーポンをつけていただきたいのですが
マイクロバブルバス無料!をつけていただきたいです
表面が高級感でよろしくおねがいします
ごログのURLと
マイクロバブルのクーポンは、下の方に三角形で
作って欲しいです。
今、裏面の料金が、5%価格になってますので
締め切りしましたら、料金の修正をよろしくおねがいします。(全部の修正ではなく
少し変更する感じです)

前回の追記で、クーポンは三角形にして、ブログのURLと書きましたが
正しくは、ブログのバーコードをつけてほしい感じです(記載する位置はお任せします)

引き続きよろしくおねがいします。
画像追加しました

ハーブハック
マイクロバブル
カットの写真

加工して丸く切り取りして裏面に使用してください
トイプードルの写真を追加しました

表面に使用してただけたらと思います
締め切りを12月8日にしました。
宜しくお願いします。
■ 選んだ理由

とても分かりやすくデザインが一目惚れしました
迅速な対応をとっていただいたのも本当に嬉しく思います。

■ 提案者全員のお礼・コメント

今回初めて利用しました
本当に皆様私のサロンのイメージにみなさん近かったので
かなり迷いました
本当にありがとうございました

```html
<!DOCTYPE html>
<html lang="ja">
<head>
<meta charset="utf-8">
<title>犬種別トリミングメニュー料金一覧</title>
<link href="https://fonts.googleapis.com/css2?family=M+PLUS+Rounded+1c:wght@500;700;800&family=Noto+Sans+JP:wght@400;500;700&display=swap" rel="stylesheet">
<style>
:root{
  --navy:#1d3c86;
  --blue:#3f79c4;
  --sky:#8fbfe8;
  --pale:#e3f0fb;
  --paler:#f3f8fd;
  --ink:#1d2433;
  --orange:#f08a1c;
  --pink:#e75f8a;
  --white:#ffffff;
}
*{box-sizing:border-box;margin:0;padding:0}
html,body{width:849px;height:1200px;overflow:hidden;background:var(--white)}
body{font-family:"Noto Sans JP",sans-serif;color:var(--ink);position:relative}
.sheet{position:absolute;inset:0;padding:0 22px}

/* header */
.top{height:78px;display:flex;align-items:center;justify-content:space-between}
.top h1{font-family:"M PLUS Rounded 1c",sans-serif;font-weight:800;font-size:25px;color:var(--navy)}
.top h1 small{font-size:12px;font-weight:500}
.tagline{display:flex;align-items:center;gap:10px;font-family:"M PLUS Rounded 1c",sans-serif;font-weight:700;color:var(--blue);font-size:17px}
.pups{width:120px;height:62px;border-radius:30px;background:linear-gradient(135deg,#f1e3cf,#d8b992)}

/* main price table */
.price{width:100%;border-collapse:collapse;font-size:14px}
.price th{background:var(--navy);color:var(--white);font-weight:700;height:36px;font-size:14px;border:2px solid var(--white)}
.price td{height:31px;border:2px solid var(--white);text-align:center;font-weight:500}
.price td.breed{text-align:left;padding-left:10px;background:var(--sky);color:var(--navy);font-weight:700;width:292px}
.price td.breed small{font-size:10px}
.price tr:nth-child(odd) td:not(.breed){background:var(--pale)}
.price tr:nth-child(even) td:not(.breed){background:var(--paler)}
.note{font-size:11px;margin:6px 0 0 4px;color:var(--navy)}

/* lower area */
.lower{position:absolute;top:566px;left:22px;right:22px;display:grid;grid-template-columns:360px 1fr;gap:18px}
.sec-title{font-family:"M PLUS Rounded 1c",sans-serif;font-weight:800;font-size:19px;color:var(--navy);border-bottom:3px solid var(--sky);padding-bottom:3px;margin-bottom:6px}
.sec-title small{font-size:11px;font-weight:500}
.list{list-style:none;font-size:14px}
.list li{display:flex;justify-content:space-between;padding:3px 8px;border-bottom:1px dotted var(--sky)}
.list li span:last-child{font-weight:700}
.list.stay{margin-bottom:8px}
.band{background:var(--blue);color:var(--white);font-weight:700;font-size:13px;padding:4px 10px;margin-bottom:4px}
.stay-row{display:flex;font-size:13px;padding:3px 8px;gap:14px}
.stay-row b{width:70px;color:var(--navy)}
.small{font-size:10px;line-height:1.5;margin-top:6px;color:#44506a}

.long-head{display:flex;gap:12px;align-items:center;border:2px solid var(--sky);border-radius:10px;padding:8px;margin-bottom:6px}
.circle{width:92px;height:92px;border-radius:50%;background:radial-gradient(circle at 40% 40%,#eef4fa,#a9c9e6);flex:none}
.seal{width:50px;height:50px;border-radius:50%;background:var(--orange);flex:none}
.long-head p{font-size:11px;line-height:1.6}
.long-head p b{color:var(--pink);font-size:14px}
.long .list li{font-size:13px;padding:3px 6px}
.long .list li span:last-child{color:var(--navy)}
.paws{display:flex;gap:10px;align-items:center;margin-top:8px}
.paw{width:34px;height:34px;border-radius:50%;background:var(--orange)}
.paws p{font-size:11px;color:var(--pink);font-weight:700}

/* footer */
.foot{position:absolute;left:0;right:0;bottom:0;height:198px;background:var(--navy);color:var(--white);display:flex;align-items:center;padding:0 22px;gap:18px}
.photo{width:230px;height:160px;border-radius:10px;background:linear-gradient(135deg,#8fa9c9,#e8ddc9)}
.shop{flex:1}
.shop .name{font-family:"M PLUS Rounded 1c",sans-serif;font-weight:800;font-size:28px;display:flex;align-items:center;gap:8px}
.shop .name i{width:18px;height:18px;border-radius:50%;background:var(--sky);display:inline-block}
.shop .tel{display:flex;align-items:center;gap:8px;font-size:30px;font-weight:700;margin:6px 0}
.shop .addr{font-size:13px}
.blog{display:flex;align-items:center;gap:10px;margin-top:10px}
.bubble{background:var(--white);color:var(--navy);font-weight:800;font-size:13px;border-radius:50%;width:78px;height:60px;display:flex;align-items:center;justify-content:center;text-align:center;line-height:1.2}
.url{font-size:17px;font-weight:700;background:var(--white);color:var(--navy);padding:4px 10px;border-radius:4px}
.map{width:150px;height:160px;border-radius:8px;background:linear-gradient(160deg,#dfe9f3,#b8cde3)}
</style>
</head>
<body>
<div class="sheet">
  <header class="top">
    <h1>犬種別トリミングメニュー料金一覧<small>（※税込価格）</small></h1>
    <div class="tagline">わんちゃんも飼い主さんも笑顔ではいてほしい・・・。<div class="pups" role="img" aria-label="犬のイラスト"></div></div>
  </header>

  <table class="price">
    <tr><th>犬種</th><th>シャンプー</th><th>シャンプー+カット</th><th>クレイ泥パック</th><th>ハーブパック</th></tr>
    <tr><td class="breed">チワワ<small>（スムース&amp;ロング）</small></td><td>2,940円</td><td>4,200円</td><td>1,800円</td><td>2,500円</td></tr>
    <tr><td class="breed">ピンシャー、イタリアングレイハウンド</td><td>2,940円</td><td>―</td><td>1,800円</td><td>2,500円</td></tr>
    <tr><td class="breed">ミニチュアダックス<small>（スムース&amp;ロング）</small></td><td>3,675円</td><td>4,725円</td><td>1,800円</td><td>2,500円</td></tr>
    <tr><td class="breed">ヨークシャーテリア、マルチーズ</td><td>3,675円</td><td>5,250円</td><td>1,800円</td><td>2,500円</td></tr>
    <tr><td class="breed">シーズー、ペキニーズ</td><td>4,200円</td><td>5,775円</td><td>2,800円</td><td>2,800円</td></tr>
    <tr><td class="breed">パピヨン、ポメラニアン</td><td>4,200円</td><td>5,775円</td><td>2,800円</td><td>2,800円</td></tr>
    <tr><td class="breed">トイプードル<small>（〜4kg）</small></td><td>4,200円</td><td>6,300円</td><td>2,800円</td><td>2,800円</td></tr>
    <tr><td class="breed">ミニチュアシュナウザー<small>（〜9kg）</small></td><td>4,800円</td><td>6,800円</td><td>2,500円</td><td>2,800円</td></tr>
    <tr><td class="breed">ビションフリーゼ<small>（〜9kg）</small></td><td>4,800円</td><td>6,800円</td><td>2,500円</td><td>2,800円</td></tr>
    <tr><td class="breed">パグ、フレンチブル、ボストンテリア</td><td>5,250円</td><td>―</td><td>2,500円</td><td>2,800円</td></tr>
    <tr><td class="breed">柴、ビーグル、コーギー、キャバリア</td><td>5,250円</td><td>―</td><td>2,500円</td><td>2,800円</td></tr>
    <tr><td class="breed">コッカースパニエル</td><td>5,250円</td><td>6,800円</td><td>2,500円</td><td>2,800円</td></tr>
    <tr><td class="breed">シェルティー</td><td>6,300円</td><td>8,400円</td><td>2,500円</td><td>2,800円</td></tr>
  </table>
  <p class="note">※追加オプションをご希望の方は、詳しくはお電話でお問い合わせ下さい。</p>

  <div class="lower">
    <div>
      <h2 class="sec-title">単品メニュー料金一覧<small>（※税込価格）</small></h2>
      <ul class="list">
        <li><span>爪切り</span><span>380円</span></li>
        <li><span>耳掃除</span><span>380円</span></li>
        <li><span>足裏バリカン</span><span>380円</span></li>
        <li><span>肛門腺絞り</span><span>380円</span></li>
        <li><span>顔周り・足周りカット</span><span>380円</span></li>
        <li><span>爪切り、耳掃除、肛門腺セット</span><span>980円</span></li>
      </ul>
      <h2 class="sec-title" style="margin-top:10px">お預かり<small>（※税込価格）</small></h2>
      <ul class="list stay">
        <li><span>1時間</span><span>480円</span></li>
        <li><span>3時間</span><span>1,280円</span></li>
        <li><span>6時間</span><span>2,580円</span></li>
      </ul>
      <div class="band">ショートステイ（一泊食事付き）</div>
      <div class="stay-row"><b>1泊2日</b><span>小型4,200円</span><span>中型6,300円</span></div>
      <div class="stay-row"><b>2日目以降</b><span>小型3,670円</span><span>中型5,250円</span></div>
      <p class="small">※お散歩・お食事は飼い主様のご指示に合わせます。<br>※ご予約はお早めにお電話でお願いいたします。</p>
    </div>

    <div class="long">
      <div class="long-head">
        <div class="circle" role="img" aria-label="トリミング中の犬の丸い写真"></div>
        <p><b>人気のロングコース</b><br>シャンプー・カットからハーブパック、マイクロバブルまで全部入りのスペシャルなコースです。毛並みも肌もふんわり仕上がります。</p>
        <div class="seal" role="img" aria-label="おすすめバッジ"></div>
      </div>
      <ul class="list">
        <li><span>チワワ、ピンシャー、イタリアングレイハウンド</span><span>8,400円</span></li>
        <li><span>ミニチュアダックス</span><span>9,450円</span></li>
        <li><span>ヨークシャーテリア、マルチーズ</span><span>10,500円</span></li>
        <li><span>シーズー、パピヨン、ポメラニアン</span><span>11,550円</span></li>
        <li><span>トイプードル</span><span>11,550円</span></li>
        <li><span>ミニチュアシュナウザー、ビションフリーゼ</span><span>12,600円</span></li>
        <li><span>パグ、フレンチブル、ボストンテリア</span><span>9,450円</span></li>
        <li><span>柴、ビーグル、コーギー、キャバリア</span><span>10,500円</span></li>
        <li><span>コッカースパニエル、シェルティー</span><span>14,700円</span></li>
      </ul>
      <div class="paws">
        <span class="paw"></span><span class="paw"></span><span class="paw"></span>
        <p>定期的トリミングは1カ月程度で来ていただくとキレイが続きます。</p>
      </div>
    </div>
  </div>

  <footer class="foot">
    <div class="photo" role="img" aria-label="サロン店内の写真"></div>
    <div class="shop">
      <div class="name"><i></i>Sora Dog</div>
      <div class="tel">
        <svg width="28" height="28" viewBox="0 0 24 24"><path fill="#ffffff" d="M6.6 10.8a15 15 0 0 0 6.6 6.6l2.2-2.2c.3-.3.7-.4 1-.2 1.1.4 2.3.6 3.6.6.6 0 1 .4 1 1V20c0 .6-.4 1-1 1A17 17 0 0 1 3 4c0-.6.4-1 1-1h3.5c.6 0 1 .4 1 1 0 1.3.2 2.5.6 3.6.1.3 0 .7-.2 1z"/></svg>
        03-0000-1234
      </div>
      <div class="addr">〒100-0000 東京都青空区1-2-3　営業時間 10:00〜19:00</div>
      <div class="blog"><span class="bubble">ブログ<br>やってます!</span><span class="url">http://blog.example.jp/sora-trimming/</span></div>
    </div>
    <div class="map" role="img" aria-label="店舗周辺の地図"></div>
  </footer>
</div>
</body>
</html>
```